Flyer for the Harvest of lanterns conference

Flyer design for an annual international conference called "VELMARK 2017". This is a conference for young adults, so we hope to produce a design that is both professional and appealing to young people in general

We'd like the flyer to showcase the conference brand logo, and clearly highlight the key information to people who will read it.

Target Market(s)

Young people, young adults

Industry/Entity Type

Religious

Font styles to use
Sans Serif

Colors

Designer to choose colors to be used in the design.

Requirements
Must have
• - Should be only one page (Vertical or Horizontal).
• - the VELMAK logo and all the information found in the attached text file. This includes: Main topic: Your sons and daughters shall prophesy,
• Dates and time, location, contact information and everything that is in the attached text file.
Nice to have
• It would be nice to see samples where the white logo is used and another where the black one is used.
Should not have
• This is NOT a folded flyer, we will be sticking it on doors and public places. And we will be printing large simple to put on walls. So only one page with few words like an add (the words are in the attached file)

```html
<!DOCTYPE html>
<html lang="en">
<head>
<meta charset="utf-8">
<title>VELMARK 2017 – Harvest of Lanterns Conference</title>
<link href="https://fonts.googleapis.com/css2?family=Roboto+Condensed:wght@400;700&family=Open+Sans:wght@400;600;700&display=swap" rel="stylesheet">
<style>
  :root {
    --navy: #24243a;
    --orange: #ee8a1d;
    --orange-deep: #e07c12;
    --ink: #1f1f1f;
    --grey-box: #ebebeb;
    --page-bg: #e9e4dc;
    --white: #ffffff;
    --line: #e3b98a;
  }
  * { margin: 0; padding: 0; box-sizing: border-box; }
  html, body { width: 1020px; height: 1200px; overflow: hidden; background: var(--page-bg); }
  .flyer {
    position: absolute; left: 86px; top: 0; width: 848px; height: 1200px;
    background: var(--white); overflow: hidden;
    font-family: "Open Sans", Arial, sans-serif; color: var(--ink);
  }
  .hero {
    position: absolute; left: 0; top: 0; width: 848px; height: 321px;
    background: linear-gradient(180deg, #e6836a 0%, #f0a468 45%, #c9735a 70%, #2d2f52 100%);
  }
  .title-band {
    position: absolute; left: 0; top: 321px; width: 848px; height: 179px; background: var(--navy);
  }
  .event-name {
    position: absolute; left: 43px; top: 344px;
    font-family: "Roboto Condensed", Arial, sans-serif; font-weight: 700;
    font-size: 72px; line-height: 1; color: var(--white); letter-spacing: 1px;
  }
  .event-subtitle {
    position: absolute; left: 45px; top: 424px;
    font-family: "Roboto Condensed", Arial, sans-serif; font-weight: 700;
    font-size: 30px; line-height: 1; color: var(--orange); text-transform: uppercase;
  }
  .brand-box {
    position: absolute; left: 600px; top: 321px; width: 194px; height: 179px;
    background: var(--grey-box); display: flex; flex-direction: column;
    align-items: center; justify-content: center; gap: 14px;
  }
  .brand-dot { width: 62px; height: 62px; border-radius: 50%; border: 3px solid var(--orange); }
  .brand-name {
    font-family: "Roboto Condensed", Arial, sans-serif; font-weight: 700;
    font-size: 30px; color: var(--navy); letter-spacing: 1px;
  }
  .theme {
    position: absolute; left: 0; width: 848px; top: 538px; text-align: center;
    font-family: "Roboto Condensed", Arial, sans-serif; font-weight: 700;
    font-size: 37px; color: var(--orange); text-transform: uppercase;
  }
  .theme-rule { position: absolute; left: 53px; top: 589px; width: 738px; height: 2px; background: var(--line); }
  .speakers-label {
    position: absolute; left: 60px; top: 640px; width: 279px; height: 50px;
    border: 2px solid var(--ink); display: flex; align-items: center; justify-content: center;
    font-family: "Roboto Condensed", Arial, sans-serif; font-weight: 700; font-size: 30px; letter-spacing: 0.5px;
  }
  .speaker-list { position: absolute; left: 93px; top: 716px; list-style: none; }
  .speaker-list li {
    font-family: "Open Sans", Arial, sans-serif; font-weight: 700; font-size: 16px;
    line-height: 46px; text-transform: uppercase; color: var(--ink);
  }
  .divider { position: absolute; left: 408px; top: 640px; width: 2px; height: 296px; background: #555; }
  .divider-arrow { position: absolute; left: 410px; top: 774px; }
  .date-box {
    position: absolute; left: 484px; top: 650px; width: 322px; height: 279px;
    background: var(--orange-deep); color: var(--white); text-align: center;
    display: flex; flex-direction: column; justify-content: center;
    font-family: "Open Sans", Arial, sans-serif;
  }
  .date-box p { font-size: 34px; line-height: 45px; }
  .date-box .strong { font-family: "Roboto Condensed", Arial, sans-serif; font-weight: 700; font-size: 34px; }
  .room {
    position: absolute; left: 0; width: 848px; top: 960px; text-align: center;
    font-family: "Roboto Condensed", Arial, sans-serif; font-weight: 700; font-size: 44px; color: var(--ink);
  }
  .room-label { color: var(--orange); }
  .venue {
    position: absolute; left: 236px; top: 1037px; width: 377px; height: 96px;
    border: 2px solid var(--line); border-top: none; text-align: center;
  }
  .venue-rule-left, .venue-rule-right { position: absolute; top: 1037px; height: 2px; background: var(--line); }
  .venue-rule-left { left: 236px; width: 72px; }
  .venue-rule-right { left: 541px; width: 72px; }
  .venue-title {
    position: absolute; left: 0; width: 848px; top: 1016px; text-align: center;
    font-family: "Roboto Condensed", Arial, sans-serif; font-weight: 700; font-size: 36px; color: var(--orange);
  }
  .venue-address { padding-top: 22px; font-size: 17px; line-height: 23px; color: #333; }
  .footer { position: absolute; left: 0; top: 1150px; width: 848px; height: 50px; }
  .footer-bg { position: absolute; left: 0; top: 0; display: block; }
  .footer-icon { display: block; flex: none; }
  .footer-phone {
    position: absolute; left: 60px; top: 0; height: 50px; display: flex; align-items: center; gap: 14px;
    font-family: "Roboto Condensed", Arial, sans-serif; font-weight: 700; font-size: 30px; line-height: 1; color: var(--white);
  }
  .footer-links {
    position: absolute; left: 460px; top: 0; height: 50px; display: flex; align-items: center; gap: 22px;
    font-size: 15px; line-height: 1; color: var(--white);
  }
  .footer-links span { display: flex; align-items: center; gap: 8px; }
  .footer-sep { display: block; width: 1px; height: 26px; background: rgba(255,255,255,0.7); }
</style>
</head>
<body>
<main class="flyer">
  <div class="hero" role="img" aria-label="Photo of a crowd raising hands and crosses in silhouette against an orange sunset sky"></div>

  <section class="title-band"></section>
  <h1 class="event-name">VELMARK 2017</h1>
  <p class="event-subtitle">Harvest of lanterns Conference</p>
  <div class="brand-box">
    <span class="brand-dot"></span>
    <span class="brand-name">VELMAK</span>
  </div>

  <h2 class="theme">Your sons and daughters shall prophesy</h2>
  <div class="theme-rule"></div>

  <div class="speakers-label">OUR SPEAKERS</div>
  <ul class="speaker-list">
    <li>Prophet Aurel Mabanza</li>
    <li>Prophet Joel Kitenge</li>
    <li>Bishop Samuel Luvuma</li>
    <li>Prophet Remy Onganda</li>
    <li>Prophet Isaac Moreno Tshibasu</li>
  </ul>

  <div class="divider"></div>
  <svg class="divider-arrow" width="14" height="22" viewBox="0 0 14 22"><polygon points="0,0 14,11 0,22" fill="#222"/></svg>

  <div class="date-box">
    <p class="strong">1st, 2nd and 3rd</p>
    <p>SEPTEMBER</p>
    <p class="strong">2017</p>
    <p>START TIME</p>
    <p class="strong">6:00PM</p>
  </div>

  <p class="room"><span class="room-label">Room:</span> Cedar Hall Ballroom</p>

  <div class="venue">
    <p class="venue-address">Lakeview Harbor Hotel<br>415 Elm Avenue<br>Brookfield, ME 04290 United States</p>
  </div>
  <div class="venue-rule-left"></div>
  <div class="venue-rule-right"></div>
  <p class="venue-title">LOCATION</p>

  <footer class="footer">
    <svg class="footer-bg" width="848" height="50" viewBox="0 0 848 50">
      <rect x="0" y="0" width="848" height="50" fill="#ee8a1d"/>
      <polygon points="0,0 430,0 412,50 0,50" fill="#262626"/>
    </svg>
    <div class="footer-phone">
      <svg class="footer-icon" width="28" height="28" viewBox="0 0 24 24" fill="none" stroke="#fff" stroke-width="2" stroke-linecap="round" stroke-linejoin="round">
        <path d="M22 16.9v3a2 2 0 0 1-2.2 2 19.8 19.8 0 0 1-8.6-3.1 19.5 19.5 0 0 1-6-6A19.8 19.8 0 0 1 2.1 4.2 2 2 0 0 1 4.1 2h3a2 2 0 0 1 2 1.7c.1.9.4 1.8.7 2.7a2 2 0 0 1-.5 2.1L8 9.8a16 16 0 0 0 6 6l1.3-1.3a2 2 0 0 1 2.1-.4c.9.3 1.8.6 2.7.7a2 2 0 0 1 1.7 2z"/>
      </svg>
      <span>+1 (555) 018 2473</span>
    </div>
    <div class="footer-links">
      <span><svg class="footer-icon" width="14" height="14" viewBox="0 0 14 14"><circle cx="7" cy="7" r="6" fill="none" stroke="#fff" stroke-width="1.5"/><rect x="4" y="5" width="6" height="4" fill="#fff"/></svg>hello@lanternhill.org</span>
      <i class="footer-sep"></i>
      <span><svg class="footer-icon" width="14" height="14" viewBox="0 0 14 14"><circle cx="7" cy="7" r="6" fill="none" stroke="#fff" stroke-width="1.5"/><circle cx="7" cy="7" r="2.5" fill="#fff"/></svg>www.velmak.org</span>
    </div>
  </footer>
</main>
</body>
</html>
```